Maple Glow Label

Design a label for new brand called Maple Glow. The specific product label :
Maple Glow Cocoa Butter Lotion. You only need to design the front label.
I have included the logo and a bottle jpeg with 2 bottles on it. Please try your best.

Requirements
Must have
• text on the label other than the logo:
cocoa butter
lotion
8.5oz/250ml

Original Moisturizing Formula
Smoothes Marks
Protect Skin

__________________________________
- ALTERNATIVE TEXT TO ALSO USE:
Smoothes Dry Skin, Blemishes & Stretch Marks
Softens Hands, Face and Body
Vitamin E

```html
<!DOCTYPE html>
<html lang="en">
<head>
<meta charset="utf-8">
<title>Maple Glow Cocoa Butter Lotion – Front Label</title>
<link rel="stylesheet" href="https://fonts.googleapis.com/css2?family=Oregano&family=Cormorant+Garamond:ital,wght@1,500&family=Kurale&display=swap">
<style>
  :root {
    --page-bg: #ffffff;
    --label-fill: #fdf3b6;
    --label-edge: #e58fbe;
    --label-edge-inner: #ee9d93;
    --brand-pink: #e0115f;
    --claim-purple: #7a3a8c;
    --title-blue: #1f6fbf;
    --title-outline: #e0115f;
    --art-peach: #f6bca0;
    --size-text: #222222;
  }
  html, body {
    margin: 0;
    padding: 0;
    overflow: hidden;
    background: var(--page-bg);
  }
  .canvas {
    position: relative;
    width: 1200px;
    height: 1000px;
    overflow: hidden;
    background: var(--page-bg);
  }
  .label-shape {
    position: absolute;
    inset: 0;
  }
  .brand-name {
    position: absolute;
    top: 198px;
    left: 0;
    width: 1200px;
    text-align: center;
    margin: 0;
    font-family: "Oregano", cursive;
    font-size: 74px;
    line-height: 1;
    color: var(--brand-pink);
  }
  .claim {
    position: absolute;
    top: 566px;
    left: 0;
    width: 1210px;
    text-align: center;
    margin: 0;
    font-family: "Cormorant Garamond", serif;
    font-style: italic;
    font-weight: 500;
    font-size: 33px;
    color: var(--claim-purple);
  }
  .product-title {
    position: absolute;
    top: 612px;
    left: 0;
    width: 1210px;
    text-align: center;
    margin: 0;
    font-family: "Oregano", cursive;
    font-weight: 400;
    font-size: 152px;
    line-height: 1;
    letter-spacing: -2px;
    color: var(--title-blue);
    -webkit-text-stroke: 2px var(--title-outline);
    transform: scaleX(0.82);
  }
  .product-type {
    position: absolute;
    top: 800px;
    left: 0;
    width: 1210px;
    text-align: center;
    margin: 0;
    font-family: "Kurale", serif;
    font-size: 56px;
    line-height: 1;
    color: var(--brand-pink);
  }
  .net-size {
    position: absolute;
    top: 874px;
    left: 0;
    width: 1210px;
    text-align: center;
    margin: 0;
    font-family: Arial, Helvetica, sans-serif;
    font-size: 13px;
    color: var(--size-text);
  }
</style>
</head>
<body>
<main class="canvas">
  <svg class="label-shape" width="1200" height="1000" viewBox="0 0 1200 1000">
    <defs>
      <radialGradient id="figure-glow" cx="0.5" cy="0.5" r="0.5">
        <stop offset="0" stop-color="var(--art-peach)" stop-opacity="0.75"/>
        <stop offset="1" stop-color="var(--art-peach)" stop-opacity="0"/>
      </radialGradient>
    </defs>
    <path class="label-outline"
          d="M600,128 C705,128 765,250 852,500 C935,725 880,907 610,907 C330,907 262,745 342,510 C428,250 495,128 600,128 Z"
          fill="var(--label-fill)" stroke="var(--label-edge)" stroke-width="9"/>
    <path class="label-inner-edge"
          d="M600,134 C701,134 760,254 846,502 C927,724 874,900 610,900 C334,900 270,744 349,512 C433,254 499,134 600,134 Z"
          fill="none" stroke="var(--label-edge-inner)" stroke-width="2"/>
    <ellipse class="figure-art" role="img"
             aria-label="Decorative line figure of a woman with peach flourishes on either side"
             cx="605" cy="480" rx="215" ry="200" fill="url(#figure-glow)"/>
  </svg>

  <h1 class="brand-name">Maple Glow</h1>
  <p class="claim">Softens Hands, Face and Body</p>
  <h2 class="product-title">Cocoa Butter</h2>
  <p class="product-type">lotion</p>
  <p class="net-size">8.5oz/250ml</p>
</main>
</body>
</html>
```